CD cover - Mantras: Endless Light Ahead

Welcome!

The album contains acoustic music with positive and affirmative lyrics.

Here's a medley of some songs.
https://files.sharevaultcdn.example/u/83104576/bela_moritz_endless_light_ahead_20150220.mp3

This music and life style is about enjoying ourselves and this game we call life. Respect, gratitude, love, forgiveness, simplicity, together these lead to a happy, blissful life. If the potential listener - when looking at the cover - gets this message, than it's perfect. Just make it simple, playful, beautiful. :)

BUT PLEASE AVOID CLICHÉS!! Come up with something original! Thank you!

Note: the front cover in case of online purchase of the album will be shown on a cell-phone for example. If the image is complicated and too detailed, it won't look like something.

The CD cover project has 4 parts:
1. CD cover front outside
2. CD cover front inside (track list)
3. CD cover back
4. CD (print on the disc)

The performer: Bela Moritz (logo attached). Please use the logo with the original colors and design the cover to go well with it.

Album title: Mantras: Endless Light Ahead
All my upcoming albums are going to be called "Mantras: something"

Track list:
1. Safe (3:49)
2. Love To All (3:48)
3. I Can Do It (4:36)
4. Dream Job (2:54)
5. Forgiveness (2:58)
6. Invisible (3:41)
7. Beautiful (3:23)
8. Gratitude (4:03)
9. Health & Happiness (3:39)
10. Comfort Zone (4:03)
11. Silently (4:38)
12. World Peace (4:17)

All songs written by Bela Moritz
Copyright Belasound 2015.
www.belasound.example

I am going to need the cover in RGB format.

That's pretty much it. If I missed something important, mail me without hesitation! Enjoy! :)

Target Market(s)

New Age spiritual people, positive thinking people.

Industry/Entity Type

Cell Phone

Requirements
Must have
• Easy to read text and logo. I'm still building the brand.
Nice to have
• Light colors
Should not have
• Any kind of negativity at all.

```html
<!DOCTYPE html>
<html lang="en">
<head>
<meta charset="utf-8">
<title>Bela Moritz – Mantras: Endless Light Ahead – CD cover</title>
<link rel="stylesheet" href="https://fonts.googleapis.com/css2?family=Parisienne&display=swap">
<style>
  :root {
    --page-bg: #ffffff;
    --sky-deep: #1b5f8f;
    --sky-mid: #3b9cc4;
    --sky-light: #8fcbd3;
    --haze: #d7e6cf;
    --cloud-cream: #f6efc4;
    --cloud-gold: #efc766;
    --cloud-amber: #e29a2e;
    --band-gold: #f1b531;
    --ink-navy: #28324a;
    --name-white: #ffffff;
    --mark-gold: #f2b22e;
  }
  * { margin: 0; padding: 0; box-sizing: border-box; }
  html, body {
    width: 1200px;
    height: 1034px;
    overflow: hidden;
    background: var(--page-bg);
  }
  .cd-cover {
    position: absolute;
    left: 81px;
    top: 50px;
    width: 1038px;
    height: 934px;
    overflow: hidden;
  }
  .sky-artwork {
    position: absolute;
    inset: 0;
    background: linear-gradient(
      to bottom,
      var(--sky-deep) 0%,
      var(--sky-mid) 30%,
      var(--sky-light) 50%,
      var(--haze) 60%,
      var(--cloud-cream) 70%,
      var(--cloud-gold) 86%,
      var(--cloud-amber) 100%
    );
  }
  .artist-mark {
    position: absolute;
    left: 50%;
    top: 92px;
    width: 150px;
    height: 150px;
    transform: translateX(-50%);
  }
  .artist-name {
    position: absolute;
    left: 0;
    right: 0;
    top: 250px;
    text-align: center;
    font-family: "Parisienne", cursive;
    font-size: 78px;
    line-height: 1;
    color: var(--name-white);
    letter-spacing: 1px;
  }
  .title-band {
    position: absolute;
    left: 0;
    right: 0;
    top: 435px;
    height: 71px;
    background: var(--band-gold);
    display: flex;
    align-items: center;
    justify-content: center;
  }
  .album-title {
    font-family: "Parisienne", cursive;
    font-weight: 400;
    font-size: 46px;
    line-height: 1;
    color: var(--ink-navy);
    letter-spacing: 1.5px;
  }
</style>
</head>
<body>
  <main class="cd-cover">
    <div class="sky-artwork" role="img" aria-label="Textured blue sky fading into soft golden sunlit clouds"></div>

    <svg class="artist-mark" viewBox="0 0 150 150" aria-hidden="true">
      <circle cx="75" cy="75" r="62" fill="none" stroke="var(--mark-gold)" stroke-width="8"/>
    </svg>
    <h1 class="artist-name">Bela Moritz</h1>

    <div class="title-band">
      <h2 class="album-title">Mantras: Endless Light Ahead</h2>
    </div>
  </main>
</body>
</html>
```